Book cover needed for Christian Non-Fiction Book

I need book cover design (eBook , Paperback, and possibly case laminate Hardcover) for use on PQL and Halvet Print.
Title: Go Forth Called
Sub-Title: Leaving Shelter and Walking in Faithful Purpose
Author: Owen Callery
Also on front cover "Forward by R. Lisel Marrow"

I like clean/simple designs. Below are links to examples of covers I like...
https://www.bookvantle.example/dp/X4821QPT7M?tag=plumwick-20&linkCode=ogi&th=1&psc=1
https://www.bookvantle.example/dp/X49KTRMWHZ?tag=plumwick-20&linkCode=ogi&th=1&psc=1
https://www.bookvantle.example/dp/X22HQC51NT?tag=plumwick-20&linkCode=ogi&th=1&psc=1
https://www.bookvantle.example/dp/X48F3WZPDR?tag=plumwick-20&linkCode=ogi&th=1&psc=1
https://www.bookvantle.example/dp/X4M7UVVCLE?tag=plumwick-20&linkCode=ogi&th=1&psc=1
https://www.bookvantle.example/dp/X2R9HNNKA6?tag=plumwick-20&linkCode=ogi&th=1&psc=1

The main idea for Go Forth Called is that God is a sending God and being "on the move" or journeying is central to God's character, and therefore God's people. I write about our hesitancy to "go," and how the Bible is full of stories about people "going" from Abraham to Jesus, to the disciples of Jesus.

The core biblical text is the Great Commission in Matthew 28:16-20, where Jesus sends out his followers, though some of them doubt.

This paragraph from the forward by R. Lisel Marrow captures the tone of the book well:
This book is a call amid the turmoil. Sacred scripture contains no shortage of narratives in which humans are pulled from their ordinary lives with an inciting incident whose stakes are high. These Biblical figures are lulled from complacency and comfort zones—and yet they are reluctant to serve because they question their ability and influence. Their lessons are relevant for us today: They, and we, are always called and sent with authority. The power of the Holy Spirit equips their “going”—and ours. It’s a sending out that looks less like mastery and more humility. It’s a sending out that is unequivocal service to others modelled in a rabbi-reformer who washed feet and touched the unclean.

I have previously published two shorter books and would be very interested in getting new covers for the old books these so that the three have a similar feel. Whichever designer I go with for "Go Forth Called" I would also want to work with on creating a "branded look" for the other two books.

Target Market(s)

Christian, Religion, Spirituality Readers

Requirements
Must have
• The front cover must have this copy...
Go Forth Called
Leaving Shelter and Walking in Faithful Purpose
Owen Callery
Forward by R. Lisel Marrow

Must be willing to do the full paperback and/or hardcover, but start with thefront cover please
Nice to have
• See attached files for some book covers I like

```html
<!DOCTYPE html>
<html lang="en">
<head>
<meta charset="utf-8">
<title>Go Forth Called — Front Cover</title>
<link rel="stylesheet" href="https://fonts.googleapis.com/css2?family=Oswald:wght@500;600&display=swap">
<style>
  :root {
    --page-bg: #ffffff;
    --cover-top: #fbf6ea;
    --cover-mid: #e4e1dc;
    --cover-bottom: #a8a8a8;
    --title-green: #3f5f32;
    --subtitle-orange: #d4521e;
    --author-ink: #2b2b28;
    --leaf-green: #7c9a4a;
    --leaf-orange: #c9672a;
    --leaf-shadow: #4a2e1e;
  }
  * { margin: 0; padding: 0; box-sizing: border-box; }
  html, body {
    width: 1022px;
    height: 1200px;
    overflow: hidden;
    background: var(--page-bg);
  }
  .canvas {
    position: relative;
    width: 1022px;
    height: 1200px;
  }
  .cover {
    position: absolute;
    left: 81px;
    top: 50px;
    width: 860px;
    height: 1100px;
    background: linear-gradient(180deg, var(--cover-top) 0%, var(--cover-top) 22%, var(--cover-mid) 55%, var(--cover-bottom) 100%);
    font-family: "Oswald", "Arial Narrow", sans-serif;
    text-align: center;
  }
  .cover-title {
    position: absolute;
    top: 48px;
    left: 0;
    right: 0;
    font-weight: 600;
    font-size: 118px;
    line-height: 1.1;
    color: var(--title-green);
    letter-spacing: 1px;
  }
  .cover-subtitle {
    position: absolute;
    top: 212px;
    left: 40px;
    right: 40px;
    font-weight: 500;
    font-size: 42px;
    line-height: 1.3;
    color: var(--subtitle-orange);
  }
  .cover-subtitle span { display: block; }
  .cover-artwork {
    position: absolute;
    top: 380px;
    left: 220px;
    width: 440px;
    height: 460px;
  }
  .cover-author {
    position: absolute;
    top: 915px;
    left: 0;
    right: 0;
    font-weight: 600;
    font-size: 40px;
    line-height: 1.2;
    color: var(--author-ink);
  }
  .cover-foreword {
    position: absolute;
    top: 970px;
    left: 0;
    right: 0;
    font-weight: 600;
    font-size: 37px;
    line-height: 1.2;
    color: var(--author-ink);
  }
</style>
</head>
<body>
  <main class="canvas">
    <section class="cover">
      <h1 class="cover-title">Go Forth Called</h1>
      <p class="cover-subtitle"><span>Leaving Shelter and Walking</span><span>in Faithful Purpose</span></p>

      <svg class="cover-artwork" viewBox="0 0 440 460" role="img" aria-label="Photograph of a green maple leaf and a fallen orange leaf floating on still water">
        <defs>
          <radialGradient id="leaf-green-tone" cx="50%" cy="50%" r="50%">
            <stop offset="0%" stop-color="var(--leaf-green)" stop-opacity="0.85"/>
            <stop offset="55%" stop-color="var(--leaf-green)" stop-opacity="0.45"/>
            <stop offset="100%" stop-color="var(--leaf-green)" stop-opacity="0"/>
          </radialGradient>
          <radialGradient id="leaf-orange-tone" cx="50%" cy="50%" r="50%">
            <stop offset="0%" stop-color="var(--leaf-orange)" stop-opacity="0.95"/>
            <stop offset="55%" stop-color="var(--leaf-shadow)" stop-opacity="0.55"/>
            <stop offset="100%" stop-color="var(--leaf-shadow)" stop-opacity="0"/>
          </radialGradient>
        </defs>
        <ellipse cx="265" cy="150" rx="150" ry="120" fill="url(#leaf-green-tone)"/>
        <ellipse cx="185" cy="310" rx="130" ry="130" fill="url(#leaf-orange-tone)"/>
      </svg>

      <p class="cover-author">Owen Callery</p>
      <p class="cover-foreword">"Forward by R. Lisel Marrow"</p>
    </section>
  </main>
</body>
</html>
```